Bright Reach Hoists

im looking for someone to help me with my letterhead design. i have already got my logo design just need help with this part

Industry/Entity Type

Construction

Colors
0255a3

Requirements
Must have
• must have all my details eg. bank details, abn and acn

```html
<!DOCTYPE html>
<html lang="en">
<head>
<meta charset="utf-8">
<title>Bright Reach Hoists — Letterhead</title>
<link href="https://fonts.googleapis.com/css2?family=Roboto+Slab:wght@400;600&display=swap" rel="stylesheet">
<style>
  :root {
    --brand: #1676c2;
    --ink: #1d1d1f;
    --rule: #8a8a8a;
    --paper: #ffffff;
  }
  * { margin: 0; padding: 0; box-sizing: border-box; }
  html, body { width: 950px; height: 1200px; overflow: hidden; background: var(--paper); }
  body { font-family: "Roboto Slab", Georgia, serif; color: var(--ink); }
  .letterhead { position: relative; width: 950px; height: 1200px; }

  .brand { position: absolute; left: 26px; top: 36px; display: flex; align-items: center; gap: 14px; }
  .brand-mark { width: 30px; height: 30px; background: var(--brand); }
  .brand-name { font-size: 30px; font-weight: 600; color: var(--ink); letter-spacing: 0.2px; }

  .header-contact { position: absolute; left: 655px; top: 27px; height: 58px; border-left: 1px solid var(--rule); padding-left: 16px; }
  .contact-line { display: flex; align-items: center; gap: 10px; font-size: 16px; line-height: 1; height: 18px; }
  .contact-line + .contact-line { margin-top: 19px; }
  .icon { width: 18px; height: 18px; flex: none; }
  .accent { color: var(--brand); }

  .footer { position: absolute; left: 0; right: 0; top: 1128px; height: 50px; font-size: 15px; }
  .footer-address { position: absolute; left: 24px; top: 0; }
  .footer-address .row { display: flex; gap: 10px; line-height: 25px; }
  .footer-address .row.indent { padding-left: 28px; }
  .footer-rule { position: absolute; top: 0; width: 1px; height: 48px; background: var(--rule); }
  .footer-rule.one { left: 300px; }
  .footer-rule.two { left: 591px; }
  .footer-reg { position: absolute; left: 376px; top: 2px; line-height: 25px; }
  .footer-contact { position: absolute; right: 24px; top: 0; text-align: right; }
  .footer-contact .row { display: flex; justify-content: flex-end; align-items: center; gap: 12px; line-height: 26px; }
</style>
</head>
<body>
<div class="letterhead">
  <header>
    <div class="brand">
      <span class="brand-mark"></span>
      <span class="brand-name">Bright Reach Hoists</span>
    </div>
    <div class="header-contact">
      <div class="contact-line">
        <svg class="icon" viewBox="0 0 20 20"><circle cx="10" cy="10" r="8.5" fill="none" stroke="var(--brand)" stroke-width="1.5"/><path d="M7.5 5.5l2 2-1 1.5c.6 1.4 1.3 2.1 2.5 2.7l1.4-1 2 2-1.4 1.6c-3.2-.4-6.4-3.6-6.8-7.2z" fill="var(--brand)"/></svg>
        <span>123-456-7890</span>
      </div>
      <div class="contact-line">
        <svg class="icon" viewBox="0 0 20 20" fill="none" stroke="var(--brand)" stroke-width="1.2"><circle cx="10" cy="10" r="8.5"/><ellipse cx="10" cy="10" rx="4" ry="8.5"/><path d="M1.5 10h17M3 5.5h14M3 14.5h14"/></svg>
        <span>www.<span>bright</span><span class="accent">reachhoists</span>.com</span>
      </div>
    </div>
  </header>

  <footer class="footer">
    <div class="footer-address">
      <div class="row">
        <svg class="icon" viewBox="0 0 20 20"><path d="M10 2L1 10h3v8h4.5v-5h3v5H16v-8h3z" fill="var(--brand)"/></svg>
        <span>Street Name City Name</span>
      </div>
      <div class="row indent"><span>State Zipcode</span></div>
    </div>
    <span class="footer-rule one"></span>
    <div class="footer-reg">
      <div><span class="accent">ABN</span> 12 456 579 123</div>
      <div><span class="accent">ACN</span> 12 456 579 123</div>
    </div>
    <span class="footer-rule two"></span>
    <div class="footer-contact">
      <div class="row">
        <svg class="icon" viewBox="0 0 22 20" style="width:22px"><rect x="5" y="1" width="12" height="5" fill="var(--brand)"/><rect x="1" y="6" width="20" height="8" rx="1.5" fill="var(--brand)"/><rect x="5" y="11" width="12" height="8" fill="#fff" stroke="var(--brand)" stroke-width="1.4"/><path d="M7.5 14h7M7.5 16.5h5" stroke="var(--brand)" stroke-width="1"/></svg>
        <span>123-456-7890</span>
      </div>
      <div class="row">
        <svg class="icon" viewBox="0 0 22 16" style="width:22px;height:16px"><rect x="1" y="2" width="20" height="12" fill="var(--brand)"/><path d="M1 2l10 7 10-7" fill="none" stroke="#fff" stroke-width="1.4"/></svg>
        <span>bright<span class="accent">reachhoists</span>@mailbox.com</span>
      </div>
    </div>
  </footer>
</div>
</body>
</html>
```